Gaming Developer Wordpress Website

I am looking for someone to design a standout website for my video game developer website. We are currently developing a strategy / sim game.
Id like the following pages:
1) Games (will have a picture icon of games that we release, gamers can click each to take them to another page specifically about that game)
2) News (this will host news on coming soon or released games and general content updates)
3) Videos (this might host videos on my games or link to my ClipVane account)
4) Company (general about, mission, vison, and other info on the team and founder)
5) Support (a form gamers can fill out for help)
Id like the ability for gamers to create an account and sign up for my company newsletter.
At some point I want to be able to add a forum to my site to drive further traffic and allow gamers to discuss my games, so please make sure this is possible.
Design and color wise:
I would like the background to be a dark color, preferably black or maybe grey. I am looking for something clean, and that properly fits the gaming space.
(Lastly, I own the domain for my site, and it is currently hosted on wordpress).

```html
<!DOCTYPE html>
<html lang="en">
<head>
<meta charset="utf-8">
<title>Novarc Studios — Home</title>
<link href="https://fonts.googleapis.com/css2?family=Source+Sans+3:wght@400;600;700&display=swap" rel="stylesheet">
<style>
:root{
  --black:#000;
  --ink:#111;
  --card:#141414;
  --panel:#171717;
  --steel:#8fa3b1;
  --steel-light:#b4c2cb;
  --white:#fff;
  --muted:#d8d8d8;
}
*{box-sizing:border-box;margin:0;padding:0}
html,body{width:1200px;height:4087px;overflow:hidden}
body{background:var(--black);color:var(--white);font-family:"Source Sans 3",Arial,sans-serif;position:relative}
.abs{position:absolute}

/* brand */
.brand{display:flex;align-items:center;gap:10px;font-weight:700;color:var(--white);white-space:nowrap}
.brand .mark{background:var(--steel);display:block}
.brand-head{left:144px;top:36px;font-size:21px}
.brand-head .mark{width:22px;height:22px}
.brand-foot{left:0;width:1200px;justify-content:center;top:3775px;font-size:32px}
.brand-foot .mark{width:32px;height:32px}

/* header */
.search{left:590px;top:16px;width:283px;height:32px;background:#0b0b0b;border:1px solid #333;font-size:11px;padding:9px 14px}
.search .btn{position:absolute;right:2px;top:2px;width:36px;height:26px;background:var(--steel);display:flex;align-items:center;justify-content:center}
.account{left:914px;top:19px;font-size:14px;display:flex;align-items:center;gap:8px}
.nav{top:67px;font-size:14px;font-weight:600}
.nav.active{text-decoration:underline;color:var(--steel-light)}

/* hero */
.hero-left{left:0;top:100px;width:600px;height:546px;background:var(--steel)}
.hero-photo{left:600px;top:100px;width:600px;height:546px;background:linear-gradient(135deg,#4e5355 0%,#747a7d 40%,#3b4d63 70%,#1f2730 100%)}
.eyebrow{left:144px;top:202px;font-size:14px;font-weight:600;color:var(--ink)}
.hero-title{left:142px;top:234px;font-size:52px;font-weight:700;color:var(--ink);letter-spacing:.5px;white-space:nowrap}
.platform{top:330px;width:120px;text-align:center;color:var(--ink);font-size:16px;font-weight:600}
.platform svg{display:block;margin:0 auto 12px}
.arrow-dot{width:32px;height:32px;border-radius:50%;display:flex;align-items:center;justify-content:center}
.btn-dark{left:146px;top:448px;width:167px;height:47px;background:var(--ink);color:var(--white);font-size:15px;font-weight:700;display:flex;align-items:center;justify-content:center}
.btn-outline{left:332px;top:448px;width:166px;height:47px;border:2px solid var(--ink);color:var(--ink);font-size:15px;font-weight:700;display:flex;align-items:center;justify-content:center}

/* section heads */
.sec-title{left:0;width:1200px;text-align:center;font-size:31px;font-weight:700}
.sec-rule{left:570px;width:60px;height:3px;background:var(--steel)}

/* game cards */
.game{top:805px;width:294px;height:371px;background:var(--card)}
.game.hover{border:1px solid var(--steel)}
.game .shot{height:225px}
.game h3{margin-top:22px;font-size:17px;font-weight:700;text-align:center}
.game p{margin:10px 18px 0;font-size:14.5px;line-height:22px;text-align:center;color:var(--muted)}
.game .more{margin-top:10px;text-align:center;font-size:13px;font-weight:700;color:var(--steel-light)}
.btn-steel{background:var(--steel);color:var(--ink);font-size:15px;font-weight:700;display:flex;align-items:center;justify-content:center}

/* forum */
.forum{left:144px;top:1431px;width:910px;height:270px;border:1.5px solid var(--steel);border-radius:14px;overflow:hidden}
.forum-head{height:62px;background:var(--steel);color:var(--ink);display:flex;align-items:center;padding:0 26px;font-size:20px;font-weight:700;gap:18px}
.forum-split{left:455px;top:62px;width:1.5px;height:208px;background:var(--steel)}
.forum-mid{left:0;top:165px;width:910px;height:1.5px;background:var(--steel)}
.topic{font-size:15px;font-weight:700;display:flex;align-items:center;gap:12px}
.badge{background:var(--steel);color:var(--ink);font-size:11px;font-weight:700;border-radius:10px;padding:1px 10px}
.stats{font-size:11px;font-weight:700}
.latest{font-size:12px;font-weight:600;line-height:22px}
.latest small{font-size:10px;font-weight:400}
.latest span{color:var(--steel-light);font-size:12px}
.dot{width:8px;height:8px;border-radius:50%;background:#333}

/* videos */
.video{top:1966px;width:286px;height:197px}
.video .frame{position:absolute;left:7px;top:7px;right:7px;bottom:7px;border:2px solid var(--white)}
.play{position:absolute;left:126px;top:81px;width:34px;height:34px;border-radius:50%;background:var(--white);display:flex;align-items:center;justify-content:center}
.slide-btn{width:28px;height:28px;border-radius:50%;background:var(--white);display:flex;align-items:center;justify-content:center}

/* newsletter */
.newsletter{left:0;top:2249px;width:1200px;height:265px;background:linear-gradient(180deg,#a9b8c2 0%,#bcc8d0 55%,#a7b6c0 100%)}
.newsletter h2{position:absolute;top:50px;width:1200px;text-align:center;font-size:31px;font-weight:700;color:var(--ink)}
.newsletter p{position:absolute;top:123px;width:1200px;text-align:center;font-size:14px;color:#222}
.email{position:absolute;left:341px;top:174px;width:391px;height:43px;background:#6d7b85;font-size:11px;color:var(--white);padding:14px 20px}
.subscribe{position:absolute;left:732px;top:174px;width:128px;height:43px;background:var(--ink);font-size:14px;font-weight:700;display:flex;align-items:center;justify-content:center}

/* news */
.news{top:2679px;width:288px;height:317px;background:var(--card)}
.news .shot{height:190px}
.news .meta{position:absolute;left:62px;top:177px;width:164px;height:26px;background:var(--steel);color:var(--ink);font-size:11px;display:flex;align-items:center;justify-content:center}
.news h3{margin-top:38px;font-size:17px;font-weight:600;text-align:center}
.news p{margin:8px 18px 0;font-size:12.5px;line-height:22px;text-align:center;color:var(--muted)}

/* contact */
.contact-photo{left:127px;top:3172px;width:417px;height:359px;background:linear-gradient(135deg,#5a2c7a 0%,#b5557b 45%,#e8a0a0 70%,#7a6cb0 100%)}
.contact-frame{left:725px;top:3190px;width:341px;height:322px;border:5px solid var(--steel)}
.contact-box{left:457px;top:3220px;width:582px;height:395px;background:var(--panel)}
.contact-title{left:505px;top:3260px;font-size:31px;font-weight:700}
.field{font-size:12px;color:var(--muted);border-bottom:1.5px solid var(--muted);padding-bottom:8px}
.send{left:924px;top:3511px;width:60px;height:60px;border-radius:50%;background:var(--steel);display:flex;align-items:center;justify-content:center}

/* footer */
.foot-nav{left:0;top:3889px;width:1200px;display:flex;justify-content:center;gap:28px;font-size:15px}
.foot-nav .sep{color:var(--muted)}
.foot-rule{left:144px;top:3937px;width:910px;height:1px;background:#2a2a2a}
.copyright{left:0;top:3957px;width:1200px;text-align:center;font-size:14px}
.social{top:3993px;width:38px;height:38px;border-radius:50%;background:var(--white);display:flex;align-items:center;justify-content:center}
.social.active{background:var(--steel)}
</style>
</head>
<body>

<!-- header -->
<div class="abs brand brand-head"><span class="mark"></span>NOVARC STUDIOS</div>
<div class="abs search">Select Here
  <span class="btn"><svg width="14" height="14" viewBox="0 0 14 14"><circle cx="6" cy="6" r="4.5" fill="none" stroke="#111" stroke-width="2"/><path d="M9.5 9.5 13 13" stroke="#111" stroke-width="2"/></svg></span>
</div>
<div class="abs account"><svg width="20" height="20" viewBox="0 0 20 20"><circle cx="10" cy="10" r="9" fill="none" stroke="#fff" stroke-width="1.5"/><circle cx="10" cy="8" r="3.2" fill="#fff"/><path d="M4.5 16c1.5-3 9.5-3 11 0" fill="#fff"/></svg>SIGN IN / REGISTER</div>
<div class="abs nav active" style="left:484px">HOME</div>
<div class="abs nav" style="left:579px">ABOUT US</div>
<div class="abs nav" style="left:699px">GAMES</div>
<div class="abs nav" style="left:799px">VIDEOS</div>
<div class="abs nav" style="left:904px">NEWS</div>
<div class="abs nav" style="left:994px">SUPPORT</div>

<!-- hero -->
<div class="abs hero-left"></div>
<div class="abs hero-photo" role="img" aria-label="Gamer wearing headphones playing at a desk with two monitors"></div>
<div class="abs arrow-dot" style="left:48px;top:327px;background:#fff"><svg width="12" height="8" viewBox="0 0 12 8"><path d="M1 7 6 2l5 5" fill="none" stroke="#111" stroke-width="1.6"/></svg></div>
<div class="abs arrow-dot" style="left:48px;top:375px;background:#111"><svg width="12" height="8" viewBox="0 0 12 8"><path d="M1 1l5 5 5-5" fill="none" stroke="#fff" stroke-width="1.6"/></svg></div>
<div class="abs eyebrow">WELCOME TO NOVARC STUDIOS</div>
<div class="abs hero-title">NOVARC STUDIOS</div>
<div class="abs platform" style="left:132px">
  <svg width="40" height="40" viewBox="0 0 40 40" fill="none" stroke="#333" stroke-width="1.6"><rect x="4" y="3" width="16" height="32"/><path d="M8 9h8M8 14h8"/><rect x="17" y="22" width="20" height="13" rx="5"/><path d="M23 28h4M25 26v4"/><circle cx="32" cy="28" r="1"/></svg>CONSOLE</div>
<div class="abs platform" style="left:241px">
  <svg width="46" height="40" viewBox="0 0 46 40" fill="none" stroke="#333" stroke-width="1.6"><rect x="2" y="3" width="42" height="27"/><path d="M2 25h42M23 30v6M14 37h18"/></svg>PC</div>
<div class="abs platform" style="left:339px">
  <svg width="26" height="40" viewBox="0 0 26 40" fill="none" stroke="#333" stroke-width="1.6"><rect x="2" y="1" width="22" height="38" rx="3"/><path d="M2 7h22M2 32h22"/><circle cx="13" cy="35.5" r="1"/></svg>MOBILE</div>
<div class="abs btn-dark">DOWNLOAD NOW</div>
<div class="abs btn-outline">AVAILABLE NOW</div>

<!-- games -->
<div class="abs sec-title" style="top:718px">GAMES LISTS</div>
<div class="abs sec-rule" style="top:772px"></div>
<div class="abs game" style="left:144px">
  <div class="shot" role="img" aria-label="Racing game scene with a red sports car at night" style="background:linear-gradient(135deg,#3b2a8a,#c2418d 55%,#e8784a)"></div>
  <h3>GAME 01</h3><p>Lorem ipsum dolor sit amet,adipiscing elit, sed do eiusmod tempor</p><div class="more">READ MORE ›</div>
</div>
<div class="abs game hover" style="left:452px">
  <div class="shot" role="img" aria-label="Adventure game scene on a grassy path" style="background:linear-gradient(160deg,#d8a24a,#6e8f3a 50%,#2f5a34)"></div>
  <h3>GAME 02</h3><p>Lorem ipsum dolor sit amet,adipiscing elit, sed do eiusmod tempor</p><div class="more">READ MORE ›</div>
</div>
<div class="abs game" style="left:760px">
  <div class="shot" role="img" aria-label="Off-road game scene with an orange truck in a desert canyon" style="background:linear-gradient(135deg,#f0d7a8,#c48a4e 50%,#6b4a30)"></div>
  <h3>GAME 03</h3><p>Lorem ipsum dolor sit amet,adipiscing elit, sed do eiusmod tempor</p><div class="more">READ MORE ›</div>
</div>
<div class="abs btn-steel" style="left:508px;top:1217px;width:184px;height:43px">VIEW MORE GAMES</div>

<!-- forums -->
<div class="abs sec-title" style="top:1337px">FORUMS</div>
<div class="abs sec-rule" style="top:1391px"></div>
<div class="abs forum">
  <div class="forum-head">
    <svg width="34" height="30" viewBox="0 0 34 30" fill="none" stroke="#111" stroke-width="1.8"><rect x="10" y="3" width="22" height="16"/><path d="M17 23h8M21 19v4"/><rect x="2" y="8" width="7" height="19"/><rect x="12" y="24" width="18" height="4"/></svg>
    PC GAMING DISCUSSIONS
    <svg style="margin-left:auto" width="28" height="28" viewBox="0 0 28 28" fill="none" stroke="#111" stroke-width="1.8"><circle cx="14" cy="14" r="12"/><path d="M8.5 11.5 14 17l5.5-5.5"/></svg>
  </div>
  <div class="abs forum-split"></div>
  <div class="abs forum-mid"></div>

  <div class="abs topic" style="left:26px;top:92px"><svg width="20" height="18" viewBox="0 0 20 18"><path d="M2 2h16v11H8l-4 4v-4H2z" fill="#ccc"/><circle cx="6.5" cy="7.5" r="1.2" fill="#111"/><circle cx="10" cy="7.5" r="1.2" fill="#111"/><circle cx="13.5" cy="7.5" r="1.2" fill="#111"/></svg>General Gaming <span class="badge">New</span></div>
  <div class="abs stats" style="left:60px;top:124px">💬 2.6K &nbsp;68.8K</div>
  <div class="abs latest" style="left:283px;top:90px">Lorem ipsum dolor<br><small>(55 minutes ago)</small> <span>Johnway</span></div>

  <div class="abs topic" style="left:498px;top:92px"><svg width="22" height="22" viewBox="0 0 22 22" fill="none" stroke="#ccc" stroke-width="1.8"><circle cx="14" cy="3" r="2" fill="#ccc"/><path d="M3 8h7l3 4-3 5M13 12l5 2M10 17l-4 4"/></svg>Shooting Gaming <span class="badge">New</span></div>
  <div class="abs stats" style="left:530px;top:124px">💬 2.6K &nbsp;68.8K</div>
  <div class="abs latest" style="left:749px;top:90px">Lorem ipsum dolor<br><small>(55 minutes ago)</small> <span>Johnway</span></div>

  <div class="abs topic" style="left:26px;top:196px"><svg width="22" height="22" viewBox="0 0 22 22" fill="none" stroke="#ccc" stroke-width="1.8"><path d="M20 2c-6 0-11 4-13 10l3 3c6-2 10-7 10-13z"/><path d="M7 12l-4 1 2 2M10 15l-1 4-2-2"/></svg>RPG Gaming <span class="badge">New</span></div>
  <div class="abs stats" style="left:60px;top:228px">💬 2.6K &nbsp;68.8K</div>
  <div class="abs latest" style="left:283px;top:194px">Lorem ipsum dolor<br><small>(55 minutes ago)</small> <span>Johnway</span></div>

  <div class="abs topic" style="left:498px;top:196px"><svg width="26" height="20" viewBox="0 0 26 20"><path d="M3 9l3-6h14l3 6v8H3z" fill="#ccc"/><rect x="7" y="5" width="12" height="4" fill="#111"/><circle cx="7" cy="13" r="1.8" fill="#111"/><circle cx="19" cy="13" r="1.8" fill="#111"/></svg>Retro Gaming <span class="badge">New</span></div>
  <div class="abs stats" style="left:530px;top:228px">💬 2.6K &nbsp;68.8K</div>
  <div class="abs latest" style="left:749px;top:194px">Lorem ipsum dolor<br><small>(55 minutes ago)</small> <span>Johnway</span></div>
</div>
<div class="abs dot" style="left:580px;top:1735px"></div>
<div class="abs dot" style="left:596px;top:1735px;background:var(--white)"></div>
<div class="abs dot" style="left:612px;top:1735px"></div>

<!-- videos -->
<div class="abs sec-title" style="top:1869px">VIDEOS</div>
<div class="abs sec-rule" style="top:1922px"></div>
<div class="abs slide-btn" style="left:88px;top:2052px"><svg width="8" height="12" viewBox="0 0 8 12"><path d="M6 1 1 6l5 5" fill="none" stroke="#111" stroke-width="1.6"/></svg></div>
<div class="abs slide-btn" style="left:1083px;top:2052px"><svg width="8" height="12" viewBox="0 0 8 12"><path d="M2 1l5 5-5 5" fill="none" stroke="#111" stroke-width="1.6"/></svg></div>
<div class="abs video" style="left:144px" role="img" aria-label="Video thumbnail of a gamer at a desk with a colorful monitor">
  <div style="position:absolute;inset:0;background:linear-gradient(135deg,#2a2a5a,#8a3aa8 55%,#e07ab0)"></div><div class="frame"></div>
  <div class="play"><svg width="12" height="14" viewBox="0 0 12 14"><path d="M2 1l9 6-9 6z" fill="#111"/></svg></div></div>
<div class="abs video" style="left:457px" role="img" aria-label="Video thumbnail of hands holding a phone playing an action game">
  <div style="position:absolute;inset:0;background:linear-gradient(135deg,#cfd6e0,#5a6c8a 50%,#1e2432)"></div><div class="frame"></div>
  <div class="play"><svg width="12" height="14" viewBox="0 0 12 14"><path d="M2 1l9 6-9 6z" fill="#111"/></svg></div></div>
<div class="abs video" style="left:768px" role="img" aria-label="Video thumbnail of a family playing console games in a cozy room">
  <div style="position:absolute;inset:0;background:linear-gradient(135deg,#3a2a1e,#a8642e 55%,#e8b060)"></div><div class="frame"></div>
  <div class="play"><svg width="12" height="14" viewBox="0 0 12 14"><path d="M2 1l9 6-9 6z" fill="#111"/></svg></div></div>

<!-- newsletter -->
<div class="abs newsletter">
  <h2>SUBSCRIBE TO OUR NEWSLETTER</h2>
  <p>Lorem ipsum dolor sit amet, consectetur adipiscing elit, sed do eiusmod tempor incididunt ut labore</p>
  <div class="email">Enter your email</div>
  <div class="subscribe">SUBSCRIBE</div>
</div>

<!-- news -->
<div class="abs sec-title" style="top:2587px">NEWS</div>
<div class="abs sec-rule" style="top:2641px"></div>
<div class="abs news" style="left:144px">
  <div class="shot" role="img" aria-label="Hands holding a phone running a mobile game" style="background:linear-gradient(135deg,#dcdcdc,#7a8a9a 50%,#3a4a5a)"></div>
  <div class="meta">August 13, 2021 &nbsp;|&nbsp; John Doe</div>
  <h3>Lorem ipsum dolor sit</h3><p>Sed ut perspiciatis unde omnis iste natus error sit voluptatem accusantium</p></div>
<div class="abs news" style="left:456px">
  <div class="shot" role="img" aria-label="Gamer in headphones facing a neon lit screen" style="background:linear-gradient(135deg,#3a1a3a,#a83a6a 50%,#5a2a5a)"></div>
  <div class="meta">August 13, 2021 &nbsp;|&nbsp; John Doe</div>
  <h3>Lorem ipsum dolor sit</h3><p>Sed ut perspiciatis unde omnis iste natus error sit voluptatem accusantium</p></div>
<div class="abs news" style="left:767px">
  <div class="shot" role="img" aria-label="Gamer at a desk playing on a monitor in a dim room" style="background:linear-gradient(135deg,#2a1e1a,#6a4a3a 50%,#1a2a3a)"></div>
  <div class="meta">August 13, 2021 &nbsp;|&nbsp; John Doe</div>
  <h3>Lorem ipsum dolor sit</h3><p>Sed ut perspiciatis unde omnis iste natus error sit voluptatem accusantium</p></div>
<div class="abs btn-steel" style="left:532px;top:3039px;width:136px;height:43px">LEARN MORE</div>

<!-- contact -->
<div class="abs contact-photo" role="img" aria-label="Backlit keyboard, mouse, headset and phone on a desk"></div>
<div class="abs contact-frame"></div>
<div class="abs contact-box"></div>
<div class="abs contact-title">CONTACT US</div>
<div class="abs field" style="left:511px;top:3340px;width:212px">John Smith</div>
<div class="abs field" style="left:768px;top:3340px;width:212px">Lorem Ipsum</div>
<div class="abs field" style="left:511px;top:3427px;width:212px">info@gmail.com</div>
<div class="abs field" style="left:768px;top:3427px;width:212px">0123-456-7890</div>
<div class="abs field" style="left:511px;top:3514px;width:425px;padding-bottom:30px">Lorem ipsum dolor sit amet,...</div>
<div class="abs send"><svg width="22" height="22" viewBox="0 0 22 22"><path d="M20 2 2 10l7 3 3 7z" fill="#111"/><path d="M20 2 9 13" stroke="#8fa3b1" stroke-width="1.5"/></svg></div>

<!-- footer -->
<div class="abs brand brand-foot"><span class="mark"></span>NOVARC STUDIOS</div>
<div class="abs foot-nav"><span>HOME</span><span class="sep">/</span><span>ABOUT US</span><span class="sep">/</span><span>GAMES</span><span class="sep">/</span><span>VIDEOS</span><span class="sep">/</span><span>NEWS</span><span class="sep">/</span><span>CONTACT</span></div>
<div class="abs foot-rule"></div>
<div class="abs copyright">Copyright 2024 - Novarc Studios &nbsp;- &nbsp;All Rights Reserved</div>
<div class="abs social active" style="left:481px" aria-label="Social profile"></div>
<div class="abs social" style="left:530px" aria-label="Social profile"></div>
<div class="abs social" style="left:579px" aria-label="Social profile"></div>
<div class="abs social" style="left:629px" aria-label="Email"><svg width="16" height="12" viewBox="0 0 16 12"><rect x="0" y="0" width="16" height="12" rx="1.5" fill="#111"/><path d="M1 1.5 8 7l7-5.5" fill="none" stroke="#fff" stroke-width="1.3"/></svg></div>
<div class="abs social" style="left:679px" aria-label="Social profile"></div>

</body>
</html>
```